Manuka Honey company needs a Upmarket, Luxury Website!

New Zealand, Taranaki based Manuka Honey company Marumaru Honey is looking for a new website, we are looking for an upmarket, luxury, serious website design. We export the highest quality quality Manuka Honey, straight from the Taranaki region.

Main export markets are Asia & Europe, also New Zealand & Australia.

Looking to have a beautiful, upmarket, serious, luxurious & graphical experience with mobile optimization in mind. Like the use of product staging/mockups

You can use copy from other websites to build the site and we will change the copy after the design is finished.

***Please include 'Honey Product' mockups in website.

*Will add illustrator files in coming days***

Feel free to make website functional in Shopify, Wordpress or WIX

Target Market(s)

Asia, Europe (main markets) New Zealand, Australia (Submarkets)

Coding

Coded - Design and coding required

Number of Pages Required

4 page

Requirements
Must have
• Home, Shop, About Us, Contact Us

Homepage to include:

Our Products
Company Video (video under construction)
What is MGO/UMF
Newsletter Opt-in

***(Not in Order)***

Please include 'Honey Product' mockups in website.
*Will add illustrator files in coming days
Nice to have
• FAQ & Partnership Inquiries (hyperlink in footer)

```html
<!DOCTYPE html>
<html lang="en">
<head>
<meta charset="utf-8">
<title>Marumaru Honey – Home</title>
<link rel="stylesheet" href="https://fonts.googleapis.com/css2?family=Open+Sans:wght@400;600;700&family=Arimo:wght@700&display=swap">
<style>
:root{
  --stage:#3b3b3b;
  --paper:#ffffff;
  --ink:#161616;
  --body:#444444;
  --gold:#c9a063;
  --rust:#c4471c;
  --hairline:#e3e3e3;
  --night:#000000;
  --card-night:#262626;
  --bar-night:#2a2a2a;
}
*{box-sizing:border-box;margin:0;padding:0}
html,body{width:1128px;height:1200px;overflow:hidden;background:var(--stage);font-family:"Open Sans",Arial,sans-serif}
.stage{position:relative;width:1128px;height:1200px}
.panel{position:absolute;top:30px;width:872px;height:1890px;transform:scale(.6039);transform-origin:0 0;background:var(--paper);overflow:hidden;color:var(--ink)}
.panel--light{left:26.6px}
.panel--dark{left:575px;background:var(--night);color:#fff}
.abs{position:absolute}

/* hero */
.hero{left:0;top:0;width:872px;height:438px;background:
  radial-gradient(ellipse at 72% 30%,#4d5a2e 0%,transparent 45%),
  radial-gradient(ellipse at 55% 68%,#d6a52a 0%,transparent 22%),
  linear-gradient(180deg,#8a93a0 0%,#6f7c86 45%,#5b6a4d 75%,#7b7a3a 100%)}
.hero::after{content:"";position:absolute;inset:0;background:linear-gradient(90deg,rgba(0,0,0,.35),rgba(0,0,0,0) 60%)}
.navbar{left:81px;top:28px;width:710px;height:62px;background:var(--paper);display:flex;align-items:center;z-index:2}
.panel--dark .navbar{background:var(--bar-night)}
.brand{position:absolute;left:14px;top:0;width:120px;height:62px;display:flex;flex-direction:column;align-items:center;justify-content:center;gap:5px;font-size:10px;font-weight:600;letter-spacing:1.2px;color:var(--ink);white-space:nowrap}
.brand-dot{width:12px;height:12px;border-radius:50%;background:var(--gold)}
.brand--seal{left:16px;top:-18px;width:98px;height:98px;border-radius:50%;background:var(--bar-night);border:2px solid var(--gold);color:var(--gold);font-size:10px;text-align:center;line-height:1.3;white-space:normal}
.menu{position:absolute;left:160px;top:0;height:62px;display:flex;align-items:center;gap:23px;font-size:12px;font-weight:600;color:var(--ink)}
.panel--dark .menu{color:#fff}
.menu .is-current{color:var(--rust)}
.cart{position:relative;width:14px;height:12px}
.cart-count{position:absolute;right:-6px;top:-5px;width:8px;height:8px;border-radius:50%;background:var(--rust);font-size:6px;color:#fff;text-align:center;line-height:8px}
.btn-contact{position:absolute;right:21px;top:17px;width:94px;height:30px;background:var(--gold);color:#fff;font-size:11px;font-weight:600;display:flex;align-items:center;justify-content:center}
.hero-copy{left:81px;top:190px;z-index:2;color:#fff}
.eyebrow{font-size:11px;font-weight:600;letter-spacing:.3px}
.hero-title{margin-top:6px;font-size:31px;font-weight:700;line-height:40px;letter-spacing:.5px}
.btn-learn{margin-top:12px;width:113px;height:46px;background:var(--rust);color:#fff;font-size:11px;font-weight:600;display:flex;align-items:center;justify-content:center}
.dots{left:408px;top:399px;display:flex;gap:4px;z-index:2}
.dots span{width:10px;height:10px;border-radius:50%;border:1px solid #fff}
.dots span:first-child{background:var(--rust);border-color:var(--rust)}

/* intro */
.h2{font-size:26px;font-weight:700;letter-spacing:.3px}
.h2 em{font-style:normal;color:var(--gold)}
.center{left:0;width:872px;text-align:center}
.mgo-title{left:81px;top:518px}
.mgo-text{left:81px;top:560px;width:240px;font-size:11px;line-height:17.5px;color:var(--body)}
.panel--dark .mgo-text{color:#ddd}
.photo-a{left:344px;top:503px;width:215px;height:304px;background:linear-gradient(160deg,#c9c2a8 0%,#8a8a6a 45%,#6f6a58 100%)}
.photo-b{left:577px;top:503px;width:215px;height:304px;background:linear-gradient(180deg,#9ab3d6 0%,#c8d4e2 25%,#4f6438 55%,#5f8a3a 100%)}

/* video */
.video-title{top:862px}
.video{left:0;top:926px;width:872px;height:317px;background:radial-gradient(ellipse at 50% 55%,#7a6a40 0%,#3c3a2c 55%,#22221c 100%)}
.play{left:414px;top:1063px;width:42px;height:42px;border-radius:50%;background:#fff}

/* products */
.products-title{top:1298px}
.card{top:1372px;width:163px;height:235px;background:var(--paper);box-shadow:0 0 6px rgba(0,0,0,.15);text-align:center}
.panel--dark .card{background:var(--card-night);box-shadow:none}
.card-img{width:120px;height:120px;margin:12px auto 0;background:radial-gradient(circle at 50% 55%,#e8a13a 0%,#d7862a 40%,#f4f0ea 72%)}
.panel--dark .card-img{background:radial-gradient(circle at 50% 55%,#e8a13a 0%,#c9771f 45%,var(--card-night) 72%)}
.card-name{margin-top:20px;font-size:13px;font-weight:600}
.card-price{margin-top:8px;font-size:13px;font-weight:600;color:var(--rust)}
.card-add{margin-top:6px;font-size:10px;font-weight:600;display:flex;justify-content:center;align-items:center;gap:5px}
.arrow{top:1475px;width:30px;height:30px;display:flex;align-items:center;justify-content:center}
.panel--dark .arrow{background:#fff;border-radius:50%}

/* newsletter */
.news-title{top:1664px;font-family:Arimo,Arial,sans-serif;font-size:25px;font-weight:700;letter-spacing:.5px}
.email{left:225px;top:1716px;width:289px;height:40px;border:1px solid #bbb;background:#fff;font-size:11px;color:#444;padding:12px 14px}
.btn-sub{left:528px;top:1716px;width:118px;height:40px;background:var(--rust);color:#fff;font-family:Arimo,Arial,sans-serif;font-size:11px;font-weight:700;display:flex;align-items:center;justify-content:center}
.social{left:406px;top:1780px;display:flex;gap:7px}
.social span{width:9px;height:9px;border-radius:50%;background:currentColor}
.rule{left:81px;top:1817px;width:710px;height:1px;background:var(--hairline)}
.panel--dark .rule{background:#2a2a2a}
.copyright{top:1848px;font-size:11px;color:#333}
.panel--dark .copyright{color:#eee}
</style>
</head>
<body>
<div class="stage">

<!-- light theme -->
<section class="panel panel--light">
  <div class="abs hero" role="img" aria-label="Beekeeper in veil holding a honeycomb frame among flowers"></div>
  <nav class="abs navbar">
    <div class="brand"><span class="brand-dot"></span>MARUMARU HONEY</div>
    <div class="menu">
      <span class="is-current">Home</span><span>Our Products</span><span>Company Video</span><span>What is MGO/UMF</span>
      <span class="cart"><svg width="14" height="12" viewBox="0 0 14 12"><path d="M1 3h12l-2 8H3z" fill="currentColor"/></svg><span class="cart-count">0</span></span>
    </div>
    <div class="btn-contact">CONTACT</div>
  </nav>
  <div class="abs hero-copy">
    <div class="eyebrow">TARANAKI BASED</div>
    <h1 class="hero-title">MANUKA HONEY COMPANY<br>MARUMARU HONEY.</h1>
    <div class="btn-learn">LEARN MORE</div>
  </div>
  <div class="abs dots"><span></span><span></span><span></span><span></span></div>

  <h2 class="abs h2 mgo-title">WHAT IS <em>MGO/UMF</em></h2>
  <p class="abs mgo-text">Sed ut perspiciatis unde omnis iste natus error sit voluptatem accusantium doloremque laudantium, totam rem aperiam, eaque ipsa quae ab illo inventore veritatis et quasi architecto beatae vitae dicta sunt explicabo. Nemo enim ipsam voluptatem quia voluptas sit aspernatur aut odit aut fugit, sed quia consequuntur magni dolores eos qui ratione voluptatem sequi nesciunt. Neque porro quisquam est, qui dolorem ipsum quia dolor sit amet, consectetur, adipisci velit, sed quia non numquam eius modi tempora incidunt ut labore et dolore magnam aliquam quaerat</p>
  <div class="abs photo-a" role="img" aria-label="Team of beekeepers standing by hives below a cliff"></div>
  <div class="abs photo-b" role="img" aria-label="Beekeepers in suits at hives on a green hillside"></div>

  <h2 class="abs h2 center video-title">COMPANY <em>VIDEO</em></h2>
  <div class="abs video" role="img" aria-label="Gloved hands lifting a frame from a beehive"></div>
  <div class="abs play"><svg width="42" height="42" viewBox="0 0 42 42"><path d="M18 16l8 5-8 5z" fill="var(--rust)"/></svg></div>

  <h2 class="abs h2 center products-title">OUR <em>PRODUCTS</em></h2>
  <div class="abs arrow" style="left:23px"><svg width="10" height="14" viewBox="0 0 10 14"><path d="M7 2L2 7l5 5" stroke="var(--gold)" fill="none" stroke-width="1.5"/></svg></div>
  <div class="abs arrow" style="left:816px"><svg width="10" height="14" viewBox="0 0 10 14"><path d="M3 2l5 5-5 5" stroke="var(--gold)" fill="none" stroke-width="1.5"/></svg></div>
  <div class="abs card" style="left:81px"><div class="card-img" role="img" aria-label="Jar of manuka honey"></div><div class="card-name">SED UT PERSPICIATIS</div><div class="card-price">$20.00</div><div class="card-add"><svg width="11" height="9" viewBox="0 0 14 12"><path d="M1 3h12l-2 8H3z" fill="currentColor"/></svg>ADD TO CART</div></div>
  <div class="abs card" style="left:262px"><div class="card-img" role="img" aria-label="Bear shaped honey bottle"></div><div class="card-name">SED UT PERSPICIATIS</div><div class="card-price">$20.00</div><div class="card-add"><svg width="11" height="9" viewBox="0 0 14 12"><path d="M1 3h12l-2 8H3z" fill="currentColor"/></svg>ADD TO CART</div></div>
  <div class="abs card" style="left:444px"><div class="card-img" role="img" aria-label="Honeycomb pieces with a honey dipper"></div><div class="card-name">SED UT PERSPICIATIS</div><div class="card-price">$20.00</div><div class="card-add"><svg width="11" height="9" viewBox="0 0 14 12"><path d="M1 3h12l-2 8H3z" fill="currentColor"/></svg>ADD TO CART</div></div>
  <div class="abs card" style="left:625px"><div class="card-img" role="img" aria-label="Small glass jar of honey"></div><div class="card-name">SED UT PERSPICIATIS</div><div class="card-price">$20.00</div><div class="card-add"><svg width="11" height="9" viewBox="0 0 14 12"><path d="M1 3h12l-2 8H3z" fill="currentColor"/></svg>ADD TO CART</div></div>

  <h2 class="abs center news-title">SUBSCRIBE TO OUR NEWSLETTER</h2>
  <div class="abs email">Email Address</div>
  <div class="abs btn-sub">SUBSCRIBE</div>
  <div class="abs social" style="color:#111"><span></span><span></span><span></span><span></span></div>
  <div class="abs rule"></div>
  <p class="abs center copyright">©Copyrights 2021 Company Name &nbsp;|&nbsp;&nbsp; All Rights Reserved</p>
</section>

<!-- dark theme -->
<section class="panel panel--dark">
  <div class="abs hero" role="img" aria-label="Beekeeper in veil holding a honeycomb frame among flowers"></div>
  <nav class="abs navbar">
    <div class="brand brand--seal">MARUMARU<br>HONEY</div>
    <div class="menu">
      <span class="is-current">Home</span><span>Our Products</span><span>Company Video</span><span>What is MGO/UMF</span>
      <span class="cart"><svg width="14" height="12" viewBox="0 0 14 12"><path d="M1 3h12l-2 8H3z" fill="currentColor"/></svg><span class="cart-count">0</span></span>
    </div>
    <div class="btn-contact">CONTACT</div>
  </nav>
  <div class="abs hero-copy">
    <div class="eyebrow">TARANAKI BASED</div>
    <h1 class="hero-title">MANUKA HONEY COMPANY<br>MARUMARU HONEY.</h1>
    <div class="btn-learn">LEARN MORE</div>
  </div>
  <div class="abs dots"><span></span><span></span><span></span><span></span></div>

  <h2 class="abs h2 mgo-title">WHAT IS <em>MGO/UMF</em></h2>
  <p class="abs mgo-text">Sed ut perspiciatis unde omnis iste natus error sit voluptatem accusantium doloremque laudantium, totam rem aperiam, eaque ipsa quae ab illo inventore veritatis et quasi architecto beatae vitae dicta sunt explicabo. Nemo enim ipsam voluptatem quia voluptas sit aspernatur aut odit aut fugit, sed quia consequuntur magni dolores eos qui ratione voluptatem sequi nesciunt. Neque porro quisquam est, qui dolorem ipsum quia dolor sit amet, consectetur, adipisci velit, sed quia non numquam eius modi tempora incidunt ut labore et dolore magnam aliquam quaerat</p>
  <div class="abs photo-a" role="img" aria-label="Team of beekeepers standing by hives below a cliff"></div>
  <div class="abs photo-b" role="img" aria-label="Beekeepers in suits at hives on a green hillside"></div>

  <h2 class="abs h2 center video-title">COMPANY <em>VIDEO</em></h2>
  <div class="abs video" role="img" aria-label="Gloved hands lifting a frame from a beehive"></div>
  <div class="abs play"><svg width="42" height="42" viewBox="0 0 42 42"><path d="M18 16l8 5-8 5z" fill="var(--rust)"/></svg></div>

  <h2 class="abs h2 center products-title">OUR <em>PRODUCTS</em></h2>
  <div class="abs arrow" style="left:38px;top:1475px"><svg width="10" height="14" viewBox="0 0 10 14"><path d="M7 2L2 7l5 5" stroke="#888" fill="none" stroke-width="1.5"/></svg></div>
  <div class="abs arrow" style="left:816px;top:1475px"><svg width="10" height="14" viewBox="0 0 10 14"><path d="M3 2l5 5-5 5" stroke="#888" fill="none" stroke-width="1.5"/></svg></div>
  <div class="abs card" style="left:81px"><div class="card-img" role="img" aria-label="Jar of manuka honey"></div><div class="card-name">SED UT PERSPICIATIS</div><div class="card-price">$20.00</div><div class="card-add"><svg width="11" height="9" viewBox="0 0 14 12"><path d="M1 3h12l-2 8H3z" fill="currentColor"/></svg>ADD TO CART</div></div>
  <div class="abs card" style="left:262px"><div class="card-img" role="img" aria-label="Bear shaped honey bottle"></div><div class="card-name">SED UT PERSPICIATIS</div><div class="card-price">$20.00</div><div class="card-add"><svg width="11" height="9" viewBox="0 0 14 12"><path d="M1 3h12l-2 8H3z" fill="currentColor"/></svg>ADD TO CART</div></div>
  <div class="abs card" style="left:444px"><div class="card-img" role="img" aria-label="Honeycomb pieces with a honey dipper"></div><div class="card-name">SED UT PERSPICIATIS</div><div class="card-price">$20.00</div><div class="card-add"><svg width="11" height="9" viewBox="0 0 14 12"><path d="M1 3h12l-2 8H3z" fill="currentColor"/></svg>ADD TO CART</div></div>
  <div class="abs card" style="left:625px"><div class="card-img" role="img" aria-label="Small glass jar of honey"></div><div class="card-name">SED UT PERSPICIATIS</div><div class="card-price">$20.00</div><div class="card-add"><svg width="11" height="9" viewBox="0 0 14 12"><path d="M1 3h12l-2 8H3z" fill="currentColor"/></svg>ADD TO CART</div></div>

  <div class="abs email" style="color:#999">Email Address</div>
  <div class="abs btn-sub">SUBSCRIBE</div>
  <div class="abs social" style="color:#fff"><span></span><span></span><span></span><span></span></div>
  <div class="abs rule"></div>
  <p class="abs center copyright">©Copyrights 2021 Company Name &nbsp;|&nbsp;&nbsp; All Rights Reserved</p>
</section>

</div>
</body>
</html>
```